VELMAR WEBSITE

need to create a new website for VELMAR ltd
the company deals with all aspects of safety products & safety wear
we need a simple website to show
ideas can be taken from following website whose products we shall distribute in kenya
www.qtw.co.uk
www.brovik.eu
www.tormanhardgear.com
www.qalvenworks.co.za

we need following tabs
1) home - basic company information
2) products - broken down to following categories ie gloves, head protection, ear protection, mouth protection, foot protection
3) contacts

the company profile is a reputable company dealing with all aspects of safety, HSE (health and safety equipment), and PPE (personal protective equipment)

the website should have the brovik logo for which we are an authorized distributor.
the brovi industrial range writeup can be picked from their website

Dear Designers, i shall be able to choose a final design in 2 weeks, sorry i have not been able to finalise this due to a personal reason

Target Market(s)

the buyers are all types of industry who care for their employees safety

Industry/Entity Type

Industrial

Requirements
Must have
• clean look, fresh look, user freindly
Nice to have
• clear images, quick links etc

```html
<!DOCTYPE html>
<html lang="en">
<head>
<meta charset="utf-8">
<title>Velmar Ltd – Safety Products &amp; Safety Wear</title>
<link href="https://fonts.googleapis.com/css2?family=Oswald:wght@400;500&family=Arimo:ital,wght@0,400;0,700;1,400&display=swap" rel="stylesheet">
<style>
:root{
  --page:#eef0f1;
  --sheet:#ffffff;
  --gold:#d99a0a;
  --gold-bright:#f0b400;
  --ink:#2b2b2b;
  --body:#4a4a4a;
  --muted:#8a8a8a;
  --line:#dcdcdc;
  --btn:#5d6266;
  --btn-dark:#45494c;
  --red:#c8281e;
  --teal:#1c6e8c;
}
*{margin:0;padding:0;box-sizing:border-box}
html,body{width:976px;height:1200px;overflow:hidden}
body{background:var(--page);font-family:"Arimo",Arial,sans-serif;color:var(--body);position:relative}
.sheet{position:absolute;left:154px;top:58px;width:669px;height:1078px;background:var(--sheet);border-radius:4px;box-shadow:0 0 6px rgba(0,0,0,.12)}
.sheet > *{position:absolute}
.brand{left:16px;top:20px;display:flex;align-items:center;gap:6px}
.brand-mark{width:14px;height:14px;background:var(--gold)}
.brand-name{font-family:"Oswald",sans-serif;font-weight:500;font-size:24px;color:var(--ink);letter-spacing:1px}
.toplinks{right:16px;top:23px;font-size:8px;color:var(--ink);display:flex;gap:8px}
.social{left:274px;top:57px;display:flex;gap:3px}
.social span{width:16px;height:16px;border-radius:50%;background:#cfd1d3}
.search-box{left:410px;top:55px;width:180px;height:20px;border:1px solid #c9c9c9;border-radius:3px;background:#fff}
.search-btn{left:598px;top:55px;width:61px;height:20px;border-radius:3px;background:var(--btn);color:#fff;font-size:8px;display:flex;align-items:center;justify-content:center}
.nav{left:0;top:95px;width:669px;height:24px;font-family:"Oswald",sans-serif;font-size:10.5px;color:var(--ink)}
.nav a{position:absolute;top:0;height:24px;line-height:24px;transform:translateX(-50%);text-decoration:none;color:inherit}
.nav a.current{left:43px;width:77px;text-align:center;background:var(--btn);color:#fff;border-radius:3px}
.hero{left:5px;top:134px;width:457px;height:240px;border-radius:4px;overflow:hidden;background:radial-gradient(circle at 70% 35%,#3a7fb0 0%,#1f3a4f 30%,#151a1e 65%,#0d0f10 100%)}
.hero-side{left:472px;top:134px;width:192px;height:240px;border-radius:4px;overflow:hidden;background:linear-gradient(160deg,#8a5a20 0%,#5b3a18 40%,#2a1c10 100%)}
.hero h1,.hero-side h2{font-family:"Oswald",sans-serif;font-weight:500;color:#fff;position:absolute;line-height:1}
.hero h1{left:21px;top:112px;font-size:38px}
.hero h1 em{font-style:normal;color:var(--gold-bright)}
.hero p{position:absolute;left:22px;top:164px;font-family:"Oswald",sans-serif;font-size:20px;color:#fff;line-height:28px}
.hero-arrows{position:absolute;left:410px;top:212px;display:flex;gap:2px}
.hero-arrows span{width:18px;height:18px;background:var(--red);display:flex;align-items:center;justify-content:center}
.hero-side h2{left:16px;top:110px;font-size:30px;line-height:30px}
.hero-side p{position:absolute;left:16px;top:178px;font-family:"Oswald",sans-serif;font-size:10.5px;color:#fff;line-height:18px}
.welcome-title{left:12px;top:390px;font-family:"Oswald",sans-serif;font-weight:400;font-size:19px;color:var(--gold)}
.welcome-text{left:12px;top:421px;width:645px;font-size:7.3px;line-height:14px}
.card{top:466px;width:201px;height:162px;border-radius:5px;overflow:hidden}
.card .t{position:absolute;left:12px;font-family:"Oswald",sans-serif;font-weight:500;line-height:1;color:#fff}
.card .t1{top:74px;font-size:27px}
.card .t2{top:103px;font-size:34px;color:var(--gold-bright)}
.card .more{position:absolute;left:13px;top:138px;font-family:"Oswald",sans-serif;font-size:14px;color:#fff}
.card-glass{left:12px;background:linear-gradient(135deg,#b79a82 0%,#6e6a66 50%,#2e3236 100%)}
.card-cap{left:235px;background:linear-gradient(135deg,#7b9cc0 0%,#c9a33a 55%,#8c8f92 100%)}
.card-pad{left:451px;background:linear-gradient(135deg,#3c5a86 0%,#b8362e 60%,#6b1a16 100%)}
.card-pad .t1{color:var(--gold-bright)}
.card-pad .t2{color:#fff}
.col-title{top:654px;font-family:"Oswald",sans-serif;font-size:16px;color:var(--gold)}
.about-img{left:14px;top:688px;width:190px;height:104px;background:linear-gradient(120deg,#8c7f72 0%,#5e5a57 50%,#2f3a4a 100%)}
.about-text{left:14px;top:806px;width:192px;font-size:7.3px;line-height:14px}
.btn{top:882px;height:20px;width:88px;border-radius:3px;background:var(--btn);color:#fff;font-size:8px;display:flex;align-items:center;justify-content:center}
.news{left:236px;width:188px}
.news-item{position:absolute;left:0;width:188px;height:60px}
.news-item .thumb{position:absolute;left:0;top:0;width:52px;height:44px}
.news-item h3{position:absolute;left:62px;top:2px;font-weight:400;font-size:8.6px;color:var(--gold)}
.news-item p{position:absolute;left:62px;top:16px;font-size:7.3px;line-height:14px}
.news-item.sep{border-bottom:1px solid var(--line)}
.client-nav{left:630px;top:660px;display:flex;gap:4px}
.quote{font-family:Georgia,serif;font-size:30px;color:#c8c8c8;line-height:1}
.client-title{left:459px;top:704px;font-size:8.6px;color:var(--gold)}
.client-img{left:462px;top:726px;width:72px;height:62px;background:linear-gradient(135deg,#c43a22 0%,#5a2a18 55%,#1c1410 100%)}
.client-side{left:549px;top:725px;width:100px;font-size:7.3px;line-height:14px}
.client-text{left:460px;top:795px;width:190px;font-size:7.3px;line-height:14px}
.client-name{left:461px;top:842px;font-size:7.3px;font-style:italic;color:var(--gold)}
.client-date{left:461px;top:854px;font-size:7.3px;font-style:italic;color:var(--muted)}
.rule{left:14px;width:641px;height:1px;background:var(--line)}
.partners{left:14px;top:952px;width:641px;height:28px;display:flex;justify-content:space-between;align-items:center}
.partner{display:flex;align-items:center;gap:5px;font-size:16px;font-weight:700;color:#3d4a55}
.partner i{display:block;width:10px;height:10px;border-radius:50%}
.footer-links{left:23px;top:1025px;font-size:7.3px;color:var(--ink);display:flex;gap:9px}
.copy{left:23px;top:1044px;font-size:7.3px;color:var(--ink)}
.footer-brand{left:546px;top:1020px;font-size:28px;font-weight:700;color:var(--teal)}
</style>
</head>
<body>
<div class="sheet">
  <div class="brand"><span class="brand-mark"></span><span class="brand-name">VELMAR</span></div>
  <div class="toplinks"><span>Home</span><span>|</span><span>About Us</span><span>|</span><span>Contact Us</span></div>
  <div class="social" aria-label="Social links"><span></span><span></span><span></span><span></span><span></span><span></span></div>
  <div class="search-box"></div>
  <div class="search-btn">Search</div>

  <nav class="nav">
    <a class="current" href="#">HOME</a>
    <a href="#" style="left:126px">ABOUT US</a>
    <a href="#" style="left:219px">PRODUCTS</a>
    <a href="#" style="left:311px">SERVICES</a>
    <a href="#" style="left:394px">NEWS</a>
    <a href="#" style="left:486px">TESTIMONIALS</a>
    <a href="#" style="left:593px">CONTACT US</a>
  </nav>

  <section class="hero" role="img" aria-label="Welder in helmet working with bright sparks">
    <h1><em>VELMAR</em> LIMITED</h1>
    <p>Deals with all aspects of safety<br>products &amp; Safety Wear</p>
    <div class="hero-arrows">
      <span><svg width="8" height="8" viewBox="0 0 8 8"><path d="M5.5 1 2.5 4l3 3" stroke="#fff" fill="none" stroke-width="1.2"/></svg></span>
      <span><svg width="8" height="8" viewBox="0 0 8 8"><path d="M2.5 1l3 3-3 3" stroke="#fff" fill="none" stroke-width="1.2"/></svg></span>
    </div>
  </section>
  <section class="hero-side" role="img" aria-label="Worker in protective suit near a furnace">
    <h2>WORKING<br>IN FIRE</h2>
    <p>DEALS WITH ALL ASPECTS OF<br>SAFETY PRODUCTS &amp; SAFETY WEAR</p>
  </section>

  <h2 class="welcome-title">WELCOME TO VELMAR</h2>
  <p class="welcome-text">It is a long established fact that a reader will be distracted by the readable content of a page when looking at its layout. The point of using Lorem Ipsum is that it has a more-or-less normal distribution of letters, as opposed to using 'Content here, content here', making it look like readable English.</p>

  <div class="card card-glass" role="img" aria-label="Worker wearing safety glasses"><span class="t t1">SAFETY</span><span class="t t2">GLASS</span><span class="more">View more Glasses</span></div>
  <div class="card card-cap" role="img" aria-label="Yellow hard hat with level tools"><span class="t t1">SAFETY</span><span class="t t2">CAP</span><span class="more">View more Cap</span></div>
  <div class="card card-pad" role="img" aria-label="Worker wearing respirator mask and red helmet"><span class="t t1">SAFETY</span><span class="t t2">NOUSE PAD</span><span class="more">View more pad</span></div>

  <h2 class="col-title" style="left:14px">ABOUT VELMAR</h2>
  <div class="about-img" role="img" aria-label="Worker in white hard hat in a factory"></div>
  <p class="about-text">Lorem Ipsum is simply dummy text of the printing and typesetting industry. Lorem Ipsum has been the indus-try's standard dummy text ever since the 1500s, when an unknown printer took a galley of type and scrambled it to make a type specimen book.</p>
  <div class="btn" style="left:15px">View More Info</div>

  <h2 class="col-title" style="left:236px">LATEST NEWS</h2>
  <div class="news" style="top:688px">
    <div class="news-item sep" style="top:0"><div class="thumb" role="img" aria-label="Worker in orange hard hat" style="background:linear-gradient(135deg,#e07a2a,#d9d2c8)"></div><h3>Lorem Ipsum is simply dummy</h3><p>Lorem Ipsum is simply dummy<br>text of the printing</p></div>
    <div class="news-item sep" style="top:65px"><div class="thumb" role="img" aria-label="Worker at industrial site" style="background:linear-gradient(135deg,#d98a30,#6a4a2a)"></div><h3>Lorem Ipsum is simply dummy</h3><p>Lorem Ipsum is simply dummy<br>text of the printing</p></div>
    <div class="news-item" style="top:132px"><div class="thumb" role="img" aria-label="Worker wearing safety goggles" style="background:linear-gradient(135deg,#c9b8a0,#7a5a40)"></div><h3>Lorem Ipsum is simply dummy</h3><p>Lorem Ipsum is simply dummy<br>text of the printing</p></div>
  </div>
  <div class="btn" style="left:240px">View More News</div>

  <h2 class="col-title" style="left:439px">HAPPY CLIENTS</h2>
  <div class="client-nav"><svg width="16" height="8" viewBox="0 0 16 8"><path d="M4 1 1 4l3 3M12 1l3 3-3 3" stroke="#888" fill="none" stroke-width="1.3"/></svg></div>
  <div class="quote" style="left:443px;top:682px">&ldquo;</div>
  <p class="client-title">Lorem Ipsum is simply dummy text</p>
  <div class="client-img" role="img" aria-label="Welder in red helmet with sparks"></div>
  <p class="client-side">Lorem Ipsum is simply dummy text of the printing and typesetting industry. Lorem Ipsum has been the industry's standard</p>
  <p class="client-text">Lorem Ipsum is simply dummy text of the printing and typesetting industry.</p>
  <div class="quote" style="left:637px;top:818px">&rdquo;</div>
  <p class="client-name">Colin Marsh</p>
  <p class="client-date">Posted on 25 may 2013</p>
  <div class="btn" style="left:461px">View More Posts</div>

  <div class="rule" style="top:934px"></div>
  <div class="partners">
    <span class="partner"><i style="background:#3a8a2a"></i>Quorvel</span>
    <span class="partner"><i style="background:#4a7a3a"></i>Brantek</span>
    <span class="partner"><i style="background:#2a7a9a"></i>Zelnova</span>
    <span class="partner"><i style="background:#2a8a5a"></i>Kestrion</span>
    <span class="partner"><i style="background:#1c4a8c"></i>Mardon</span>
  </div>
  <div class="rule" style="top:1002px;background:#eaeaea"></div>

  <div class="footer-links"><span>Home</span><span>|</span><span>About Us</span><span>|</span><span>Products</span><span>|</span><span>Services</span><span>|</span><span>News</span><span>|</span><span>Testimonials</span><span>|</span><span>Contact Us</span></div>
  <p class="copy">Copyright © 2013. Velmar. All rights reserved</p>
  <div class="footer-brand">Brovik</div>
</div>
</body>
</html>
```